Design a Product Label for a Natural Deodorant Product

This brief is for the development of a product label for a natural deodorant product that we are creating. The requirement is for a sticker label that will be applied to the package. Full details of the project are provided in the attached briefing document.

Target Market(s)

Those seeking an alternative to chemical laden deodorants. Interested in natural products with minimal waste etc.

Industry/Entity Type

Skin Care

Requirements
Must have
• On brand. Simple.

```html
<!DOCTYPE html>
<html lang="en">
<head>
<meta charset="utf-8">
<title>Tall Rimu Natural Deodorant Label</title>
<link rel="stylesheet" href="https://fonts.googleapis.com/css2?family=Barlow+Semi+Condensed:wght@400;500;600;700&family=Fredoka:wght@700&display=swap">
<style>
  :root {
    --ink: #000000;
    --paper: #ffffff;
    --mint: #34e48f;
    --clay: #e09c5e;
    --gold: #bf9658;
    --body-font: "Barlow Semi Condensed", Arial, sans-serif;
    --display-font: "Fredoka", "Arial Rounded MT Bold", sans-serif;
  }
  * { margin: 0; padding: 0; box-sizing: border-box; }
  html, body { width: 1200px; height: 1200px; overflow: hidden; background: var(--paper); }
  .canvas { position: relative; width: 1200px; height: 1200px; font-family: var(--body-font); color: var(--ink); }

  .option-number { position: absolute; left: 34px; top: 12px; font-family: var(--body-font); font-weight: 400; font-size: 76px; letter-spacing: 6px; }

  .jar-lid, .jar-body { position: absolute; background: var(--ink); }
  .jar-lid { top: 586px; height: 162px; width: 512px; }
  .jar-body { top: 754px; height: 271px; width: 512px; }
  .jar--front { left: 117px; }
  .jar--back { left: 653px; }

  /* Front label */
  .front-label { position: absolute; left: 156px; top: 775px; width: 427px; height: 229px; background: var(--clay); }
  .flavour-panel { position: absolute; left: 0; top: 0; width: 151px; height: 144px; background: var(--mint); }
  .flavour-list { position: absolute; left: 18px; top: 56px; font-family: var(--display-font); font-weight: 700; font-size: 19px; line-height: 22px; letter-spacing: 0.5px; transform: rotate(-15deg); transform-origin: left top; }
  .divider-v { position: absolute; background: var(--ink); width: 2px; }
  .divider-h { position: absolute; background: var(--ink); height: 2px; }
  .product-name { position: absolute; left: 165px; top: 6px; font-family: var(--display-font); font-weight: 700; font-size: 88px; line-height: 88px; letter-spacing: 1px; }
  .product-line { position: absolute; left: 166px; top: 92px; font-weight: 500; font-size: 21px; line-height: 23px; letter-spacing: 0.6px; }
  .claims { position: absolute; left: 14px; top: 153px; font-weight: 500; font-size: 17px; line-height: 22px; letter-spacing: 0.9px; }
  .net-weight { position: absolute; left: 359px; top: 176px; font-weight: 400; font-size: 20px; letter-spacing: 1px; }

  /* Seal sticker */
  .seal { position: absolute; left: 0; top: 0; width: 1200px; height: 1200px; pointer-events: none; }
  .seal-text { font-family: var(--body-font); font-weight: 400; font-size: 22px; fill: var(--ink); }
  .seal-brand { font-family: var(--body-font); font-weight: 700; font-size: 30px; letter-spacing: 2px; fill: var(--gold); }

  /* Back label */
  .back-label { position: absolute; left: 692px; top: 775px; width: 426px; height: 229px; background: var(--clay); }
  .contact-strip { position: absolute; left: 90px; top: 0; width: 44px; height: 229px; background: var(--ink); }
  .vertical { position: absolute; writing-mode: vertical-rl; transform: rotate(180deg); white-space: nowrap; }
  .contact-lines { left: 8px; bottom: 16px; color: var(--clay); font-weight: 500; font-size: 13px; line-height: 15px; letter-spacing: 0.4px; }
  .cause-lines { left: 137px; bottom: 16px; font-weight: 600; font-size: 12px; line-height: 18px; letter-spacing: 1.8px; }
  .info-block { position: absolute; left: 203px; top: 11px; font-weight: 400; font-size: 13.5px; line-height: 16.6px; letter-spacing: 0.5px; }
  .info-heading { font-weight: 700; letter-spacing: 0.8px; }
  .info-gap { height: 9px; }
</style>
</head>
<body>
<main class="canvas">
  <div class="option-number">3)</div>

  <div class="jar-lid jar--front"></div>
  <div class="jar-body jar--front"></div>
  <div class="jar-lid jar--back"></div>
  <div class="jar-body jar--back"></div>

  <section class="front-label">
    <div class="flavour-panel"></div>
    <div class="flavour-list">FLAVOUR1<br>FLAVOUR2</div>
    <div class="divider-v" style="left:151px; top:13px; height:131px;"></div>
    <div class="divider-h" style="left:12px; top:143px; width:403px;"></div>
    <div class="divider-v" style="left:328px; top:143px; height:76px;"></div>
    <div class="product-name">NAME</div>
    <div class="product-line">a NATURAL DEODORANT<br>by TALL RIMU</div>
    <div class="claims">HANDMADE IN NEW ZEALAND,<br>NATURAL, ZERO WASTE,<br>ALUMINUM FREE</div>
    <div class="net-weight">60g</div>
  </section>

  <svg class="seal" viewBox="0 0 1200 1200" xmlns="http://www.w3.org/2000/svg">
    <defs>
      <path id="seal-ring" d="M232 210 A148 148 0 0 1 232 506 A148 148 0 0 1 232 210"/>
    </defs>
    <circle cx="232" cy="358" r="170" fill="var(--mint)"/>
    <rect x="190" y="500" width="85" height="278" fill="var(--mint)"/>
    <text class="seal-text"><textPath href="#seal-ring" startOffset="12" textLength="395" lengthAdjust="spacing">Visit us: tallrimu.com</textPath></text>
    <text class="seal-text"><textPath href="#seal-ring" startOffset="475" textLength="398" lengthAdjust="spacing">Follow us: tallrimu_nz</textPath></text>
    <text class="seal-brand" x="232" y="369" text-anchor="middle">TALL RIMU</text>
  </svg>

  <section class="back-label">
    <div class="contact-strip">
      <div class="vertical contact-lines">VISIT US: tallrimu.com<br>FOLLOW US: tallrimu_nz</div>
    </div>
    <div class="vertical cause-lines">[XX] CENTS OF EVERY<br>PURCHASE GO TOWARDS<br>KAURI TREE RESTORATION.</div>
    <div class="info-block">
      <div class="info-heading">INGREDIENTS:</div>
      Arrowroot powder, baking soda,<br>
      coconut oil, shea butter, sweet<br>
      almond oil, diatomaceous earth,<br>
      essential oils, [bees wax]
      <div class="info-gap"></div>
      <div class="info-heading">DIRECTIONS:</div>
      [Name] is a luscious deodorant<br>
      paste that contains no nasty<br>
      chemicals &amp; neutralises odour<br>
      naturally. Massage a small amount<br>
      under your arms for all day<br>
      protection. Store in a cool place.
    </div>
  </section>
</main>
</body>
</html>
```